Bref créative
tri-fold brochures and business card designs
New Bravoline company selling wall panels
marketing material
New company looking for marketing print material for display in retail locations and tradshows.
Home and Garden
Consumers and B2B retailers
tri-fold brochure and business card designs.
Please review website for ideas www.murelune7k.com.
I have most of images as high resolution. I have similar brochure from partner in Australia but would like to diferentiate a little. Be creative.
This image should be used for business card design, I think looks the best, but you will have to play with the black side color and incorporate the logo with contact info.
here is the brochure cover used from our Australia partner but I would like to include same layout of all images but on the inside of brochure, I will need to upload additional 4 designs.
Also I have my own bullet points.
Plimsora logo and my company logo which should be used on back cover to say Plimsora by my company logo..
Plimsora logo
here is Plimsora logo as jpeg, not sure which is needed.
My front cover bullet points
I would like to see how this image could be incorporated on the front cover of brochure where the Logo is positioned..
Try this image on back cover to see how it looks.
Should have my contact info like on website with my company logo. see website.
Images
I would like to see the look of the image boxes look like my catalogue images with the name and tile inset which I will upload
Plimsora tile design images 1 of 2 zip files
Panel inset tiles zip file 2 of 2
I need the 2 page of front side of brochure to have the ecoproduct info from my website www.murelune7k.com

```html
<!DOCTYPE html>
<html lang="en">
<head>
<meta charset="utf-8">
<title>Plimsora business card</title>
<link href="https://fonts.googleapis.com/css2?family=Open+Sans:wght@400;600&display=swap" rel="stylesheet">
<style>
  :root {
    --page: #ffffff;
    --slate: #4a5a63;
    --paper: #f1f2f1;
    --ink: #3d4e5c;
    --logo-grey: #8d9297;
    --rule: #c9cccd;
    --white: #ffffff;
  }
  html, body {
    margin: 0;
    padding: 0;
    width: 1200px;
    height: 900px;
    overflow: hidden;
    background: var(--page);
    font-family: "Open Sans", Arial, sans-serif;
  }
  .canvas {
    position: relative;
    width: 1200px;
    height: 900px;
  }
  .card {
    position: absolute;
    top: 300px;
    width: 502px;
    height: 288px;
    box-shadow: 0 3px 6px rgba(0,0,0,0.18);
  }
  .card-front {
    left: 77px;
    background: var(--slate);
  }
  .card-back {
    left: 600px;
    background: var(--paper);
  }
  .brand-front {
    position: absolute;
    left: 0;
    width: 100%;
    top: 104px;
    text-align: center;
    color: var(--white);
  }
  .brand-front .wordmark {
    font-size: 46px;
    font-weight: 400;
    letter-spacing: 0.5px;
    line-height: 1;
  }
  .brand-front .tagline {
    margin-top: 12px;
    font-size: 10px;
    letter-spacing: 3px;
  }
  .brand-back {
    position: absolute;
    left: 43px;
    top: 116px;
    width: 132px;
    text-align: center;
    color: var(--logo-grey);
  }
  .brand-back .wordmark {
    font-size: 28px;
    font-weight: 400;
    line-height: 1;
  }
  .brand-back .tagline {
    margin-top: 7px;
    font-size: 7px;
    letter-spacing: 2px;
    color: var(--ink);
  }
  .divider {
    position: absolute;
    left: 228px;
    top: 43px;
    width: 1px;
    height: 204px;
    background: var(--rule);
  }
  .contact {
    position: absolute;
    left: 302px;
    top: 64px;
    color: var(--ink);
  }
  .contact .name {
    margin: 0;
    font-size: 21px;
    font-weight: 400;
    line-height: 1.1;
  }
  .contact .role {
    margin: 2px 0 14px;
    font-size: 13px;
  }
  .contact .details {
    margin: 0;
    font-size: 11.5px;
    line-height: 16px;
  }
  .contact .details + .details {
    margin-top: 4px;
  }
</style>
</head>
<body>
<div class="canvas">
  <section class="card card-front">
    <div class="brand-front">
      <div class="wordmark">Plimsora</div>
      <div class="tagline">Bravo line</div>
    </div>
  </section>

  <section class="card card-back">
    <div class="brand-back">
      <div class="wordmark">Plimsora</div>
      <div class="tagline">Bravo line</div>
    </div>
    <div class="divider"></div>
    <div class="contact">
      <h1 class="name">Anselm Korvid</h1>
      <div class="role">Designation</div>
      <p class="details">Cell: 640 2281 904 517<br>e-mail: hello@plimsora.com</p>
      <p class="details">Plimsora<br>418 Fenwick Rd.<br>PO Box 53307, Alder Bay, ON<br>Tel: 705-283-6159</p>
    </div>
  </section>
</div>
</body>
</html>
```